Knife Group for Tarn, Vole, & Orla Knives

I have a new KW group set-up and I only have 40 members. I want to grow it by making sure I have it set-up correctly and optimize it and improve the looks. I want members to feel comfortable to post ideas, comments, pictures, etc. I have it set-up as a club that is closed until a person joins. Is it best to be closed or public for what I am doing? I sell knives on Tradlo under seller ID rkholm. I also want my KW group to feed traffic to my Tradlo store. I also have a stand alone web store using shopzel @ http://www.shopzel.example/edgeline-blades/ This will soon be updated to URL, holmsedgeworks.example Look at other KW knife groups to make my group better over time.

Target Market(s)

Knife collectors of Tarn, Vole, and Orla knives. Also any person interested in People wanting to learn more about knife collecting and they can see and post pictures of mint rare knives.

Font styles to use
Sans Serif

Colors
0255a3
ec1f27

Requirements
Must have
• Insure I have set-up my KW group correctly to target the most people. It was set-up from my page. Is there a way to only have a group, but not the page? Improve the looks of the landing page and add any unique features. I also want a landing page that stands out from others. I want it easy as possible for people to join. I am unable to boost post even if I pay KW as they send emails that boost not arrived because I am selling knives which is not true.
Nice to have
• Is it possible to have the language be for the country the person is seeing it in or does KW do that automatically? My 2 favorite colors are blue and red. I want to site to look excellent with the best colors. I am easy to work with. I want the designer to think and use their ideas along with what I want to improve what I have started.

```html
<!DOCTYPE html>
<html lang="en">
<head>
<meta charset="utf-8">
<title>Edgeline Knife Club – Group Cover</title>
<link rel="stylesheet" href="https://fonts.googleapis.com/css2?family=Roboto:wght@700;900&family=Montserrat:wght@700&family=PT+Sans:wght@700&display=swap">
<style>
  :root {
    --brand-blue: #0255a3;
    --sea-blue: #1a63bd;
    --brand-red: #ec1f27;
    --white: #ffffff;
    --page-bg: #d6d6d6;
    --avatar-grey: #474747;
    --name-grey: #555555;
    --wood-dark: #5a4636;
    --wood-light: #8d7a68;
    --gold: #c08a1e;
  }
  * { margin: 0; padding: 0; box-sizing: border-box; }
  html, body { width: 1200px; height: 943px; overflow: hidden; }
  body { background: var(--page-bg); position: relative; font-family: "Roboto", Arial, sans-serif; }

  .group-cover {
    position: absolute; left: 86px; top: 214px;
    width: 1029px; height: 462px;
    background: var(--white);
  }
  .cover-banner {
    position: absolute; left: 0; top: 0;
    width: 1029px; height: 380px; overflow: hidden;
  }
  .cover-art { position: absolute; inset: 0; }

  .brand-plate {
    position: absolute; left: 17px; top: 0;
    width: 236px; height: 104px;
    background: #3a2a22;
    padding: 10px;
  }
  .brand-plate-inner {
    width: 100%; height: 100%;
    background: #e9e9e9;
    display: flex; align-items: center; justify-content: center; gap: 8px;
    font-family: "Roboto", Arial, sans-serif; font-weight: 700;
    font-size: 18px; line-height: 1; color: var(--avatar-grey);
    white-space: nowrap;
  }
  .brand-mark { width: 14px; height: 14px; background: var(--brand-blue); flex: none; }

  .offer-tag {
    position: absolute; left: 663px; top: 250px;
    width: 254px; height: 34px;
    background: var(--brand-red); color: var(--white);
    font-weight: 900; font-size: 20px; letter-spacing: 0.3px;
    display: flex; align-items: center; justify-content: center;
    white-space: nowrap;
  }
  .offer-headline {
    position: absolute; left: 663px; top: 301px;
    color: var(--brand-red); font-weight: 900;
    font-size: 21px; line-height: 21.5px; letter-spacing: 0.3px;
    white-space: nowrap;
  }
  .store-link {
    position: absolute; left: 663px; top: 351px;
    color: var(--brand-red); font-weight: 700; font-size: 15px;
    white-space: nowrap;
  }

  .profile-frame {
    position: absolute; left: 37px; top: 226px;
    width: 222px; height: 222px;
    background: var(--white); padding: 10px;
  }
  .profile-slot {
    width: 202px; height: 202px;
    background: var(--avatar-grey); color: var(--white);
    font-family: "Montserrat", Arial, sans-serif; font-weight: 700;
    font-size: 18px; line-height: 20px; text-align: center;
    display: flex; align-items: center; justify-content: center;
  }
  .company-name {
    position: absolute; left: 296px; top: 400px;
    font-family: "PT Sans", Arial, sans-serif; font-weight: 700;
    font-size: 32px; color: var(--name-grey);
    white-space: nowrap;
  }
</style>
</head>
<body>
  <section class="group-cover">
    <div class="cover-banner">
      <svg class="cover-art" width="1029" height="380" viewBox="0 0 1029 380">
        <defs>
          <linearGradient id="woodTone" x1="0" y1="0" x2="1" y2="1">
            <stop offset="0" stop-color="var(--wood-light)"/>
            <stop offset="0.6" stop-color="var(--wood-dark)"/>
            <stop offset="1" stop-color="#3f5f8c"/>
          </linearGradient>
          <linearGradient id="seaTone" x1="0" y1="0" x2="0" y2="1">
            <stop offset="0" stop-color="var(--sea-blue)"/>
            <stop offset="1" stop-color="var(--brand-blue)"/>
          </linearGradient>
        </defs>
        <rect width="1029" height="380" fill="url(#seaTone)"/>
        <path class="knife-photo" role="img" aria-label="Photo of a collectible folding knife with inlaid turquoise handle on a display stand over a wooden table"
              d="M0 0 H1029 V60 C760 170 480 230 260 225 C160 222 70 212 0 198 Z" fill="url(#woodTone)"/>
        <path class="swoosh-red" d="M0 198 C70 212 160 222 260 225 C480 230 760 170 1029 60 V98 C780 210 520 262 300 262 C190 262 80 250 0 236 Z" fill="var(--brand-red)"/>
        <path class="swoosh-white" d="M0 254 C90 280 200 300 300 300 C560 300 800 170 1029 14 V30 C800 190 560 312 300 312 C200 312 90 292 0 268 Z" fill="var(--white)"/>
        <circle class="guarantee-seal" cx="858" cy="62" r="50" fill="var(--gold)"/>
      </svg>

      <div class="brand-plate">
        <div class="brand-plate-inner">
          <span class="brand-mark"></span>
          <span>Edgeline Knife Club</span>
        </div>
      </div>

      <div class="offer-tag">FREE SHIPPING IN U.S</div>
      <div class="offer-headline">SHARP DEALS ON<br>COLLECTIBLE KNIVES</div>
      <div class="store-link">http://www.shopzel.example/edgeline-blades/</div>
    </div>

    <div class="profile-frame">
      <div class="profile-slot">PROFILE<br>IMAGE</div>
    </div>
    <div class="company-name">Company Name</div>
  </section>
</body>
</html>
```